Need an awesome Modern Facebook and Twitter cover page

We are looking for a redesign for our facebook and twitter cover to coincide with our new design.

```html
<!DOCTYPE html>
<html lang="en">
<head>
<meta charset="utf-8">
<title>TermWise Social Cover</title>
<link rel="stylesheet" href="https://fonts.googleapis.com/css2?family=Open+Sans:wght@700;800&family=Poppins:wght@500;600&display=swap">
<style>
  :root {
    --page-bg: #ffffff;
    --slate-dark: #2b2d31;
    --slate-mid: #3c3f44;
    --slate-shape: #33363b;
    --accent-blue: #1e90d6;
    --text-white: #ffffff;
    --photo-warm: #7b7468;
    --photo-cool: #3f4a55;
  }
  * { margin: 0; padding: 0; box-sizing: border-box; }
  html, body {
    width: 880px;
    height: 1200px;
    overflow: hidden;
    background: var(--page-bg);
  }
  .canvas {
    position: relative;
    width: 880px;
    height: 1200px;
  }
  .cover {
    position: absolute;
    left: 20px;
    top: 440px;
    width: 840px;
    height: 320px;
    overflow: hidden;
    background: linear-gradient(135deg, var(--slate-mid) 0%, var(--slate-dark) 70%);
    box-shadow: 0 4px 14px rgba(0,0,0,0.25);
  }
  .cover-shapes,
  .cover-photo {
    position: absolute;
    inset: 0;
  }
  .brand-name {
    position: absolute;
    left: 128px;
    top: 50px;
    font-family: "Open Sans", sans-serif;
    font-weight: 700;
    font-size: 22px;
    color: var(--accent-blue);
    letter-spacing: 0.2px;
  }
  .headline {
    position: absolute;
    left: 128px;
    top: 92px;
    font-family: "Open Sans", sans-serif;
    font-weight: 800;
    line-height: 1.1;
  }
  .headline-main {
    display: block;
    font-size: 34px;
    color: var(--text-white);
  }
  .headline-accent {
    display: block;
    font-size: 36px;
    color: var(--accent-blue);
  }
  .tagline {
    position: absolute;
    left: 208px;
    top: 238px;
    font-family: "Poppins", sans-serif;
    font-weight: 600;
    font-size: 24px;
    color: var(--text-white);
  }
  .badge {
    position: absolute;
    left: 450px;
    top: 212px;
    width: 86px;
    height: 86px;
    border-radius: 50%;
    background: var(--accent-blue);
    border: 5px solid var(--text-white);
  }
  .contact {
    position: absolute;
    left: 563px;
    top: 231px;
    font-family: "Poppins", sans-serif;
    font-weight: 500;
    font-size: 17px;
    line-height: 25px;
    color: var(--text-white);
  }
</style>
</head>
<body>
<main class="canvas">
  <section class="cover">
    <svg class="cover-shapes" width="840" height="320" viewBox="0 0 840 320" aria-hidden="true">
      <polygon points="0,0 90,0 40,150 0,220" fill="var(--slate-shape)"/>
      <polygon points="40,150 120,320 0,320 0,220" fill="#2f3236"/>
      <polygon points="240,0 330,0 300,90" fill="#41444a"/>
    </svg>
    <svg class="cover-photo" width="840" height="320" viewBox="0 0 840 320" role="img" aria-label="Photo of hands typing on a laptop with a coffee cup on a wooden desk">
      <defs>
        <linearGradient id="photoTone" x1="0" y1="0" x2="1" y2="1">
          <stop offset="0" stop-color="var(--photo-cool)"/>
          <stop offset="0.55" stop-color="var(--photo-warm)"/>
          <stop offset="1" stop-color="#9a8c78"/>
        </linearGradient>
      </defs>
      <polygon points="540,0 840,0 840,320 478,320" fill="url(#photoTone)"/>
      <line x1="537" y1="0" x2="475" y2="320" stroke="var(--text-white)" stroke-width="3"/>
    </svg>

    <div class="brand-name">TermWise</div>
    <h1 class="headline">
      <span class="headline-main">LEARN AND ACHIEVE</span>
      <span class="headline-accent">SUCCESS</span>
    </h1>
    <p class="tagline">Online Solutions</p>
    <div class="badge" aria-hidden="true"></div>
    <p class="contact">+1 555-014-0182<br>www.termwise-learn.com</p>
  </section>
</main>
</body>
</html>
```